Trifold Leaflet - Osteopathy

Trifold Leaflet (A4 size paper) to provide information and promote an established English seafront osteopathy clinic.
I would like a simple modern design to reflect the seafront location and the caring nature of osteopathy treatment. The design needs to be not be generic or too corporate.
At the top of the front page in a large font should be the word "Osteopathy" as it will be displayed in a rack of leaflets (photo attached) and needs to be eye-catching.
I have attached a logo file and some examples of the kinds of designs that I like- but i'm very open to your expert ideas!
Also attached is a photo of the location- a bit of an ugly building but right on the beach, it would be great if this location could be emphasized!
The Word files: Leaflets word-inside.doc & Leaflets word-outside.doc uploaded show the content that I'd like- this is definitely not set in stone and I appreciate that less content is probably needed. Feel free to include/leave out whatever you feel is right.
More info on the practice can be found on my website:
www.harrowdenbackcare.com
The shutterstock images are ones that I have previously bought the rights to use, but only use them if you think they suit you design- I have included them i case they are of use to you.
Target Market(s)
Any adult.
Industry/Entity Type
Building
Look and feel
Each slider illustrates characteristics of the customer's brand and the style your logo design should communicate.

```html
<!DOCTYPE html>
<html lang="en">
<head>
<meta charset="utf-8">
<title>Harrowden Backcare – Osteopathy Leaflet</title>
<link rel="stylesheet" href="https://fonts.googleapis.com/css2?family=Open+Sans:wght@400;600;700&display=swap">
<style>
  :root {
    --page: #ffffff;
    --panel-grey: #9b9b9b;
    --band-grey: #939393;
    --ink-dark: #2a2a2a;
    --ink-soft: #4a4a4a;
    --headline: #474747;
    --white: #ffffff;
    --clinic-red: #a3090f;
    --photo-light: #f3efe9;
    --photo-mid: #dcd3c8;
    --photo-green: #b9c4a8;
    --photo-skin: #c99f86;
    --photo-shadow: #6f6a66;
  }
  * { margin: 0; padding: 0; box-sizing: border-box; }
  html, body {
    width: 1200px; height: 960px; overflow: hidden;
    background: var(--page);
    font-family: "Open Sans", Arial, sans-serif;
  }
  .leaflet {
    position: absolute; left: 96px; top: 122px;
    width: 1008px; height: 714px;
    background: var(--panel-grey);
    box-shadow: 0 4px 14px rgba(0,0,0,0.25);
    overflow: hidden;
  }
  .leaflet-shapes { position: absolute; inset: 0; }
  .intro {
    position: absolute; left: 42px; top: 46px; width: 640px;
    color: var(--white); font-size: 11.4px; line-height: 16px;
  }
  .intro p + p { margin-top: 16px; }
  .headline {
    position: absolute; left: 72px; top: 272px;
    color: var(--headline); font-weight: 400; line-height: 1;
  }
  .headline span { display: block; }
  .headline .line-1 { font-size: 25px; }
  .headline .line-2 { font-size: 25px; margin: 8px 0 0 42px; }
  .headline .line-3 { font-size: 34px; margin: 8px 0 0 4px; }
  .treating {
    position: absolute; left: 136px; top: 454px;
    width: 196px; height: 148px;
    background: var(--clinic-red); color: var(--white);
    padding: 14px 8px; font-weight: 700; font-size: 13.4px; line-height: 19px;
  }
  .treating h3 { font-size: 14px; font-weight: 700; }
  .treating ul { list-style: none; text-transform: uppercase; }
  .brand {
    position: absolute; left: 72px; top: 672px;
    display: flex; align-items: center; gap: 8px;
    color: #6a6a6a; font-size: 19px; font-weight: 400;
  }
  .brand-dot { width: 10px; height: 10px; border-radius: 50%; background: var(--clinic-red); }
  .regulation {
    position: absolute; left: 360px; top: 270px; width: 284px;
    color: var(--ink-dark); font-size: 11.2px; line-height: 15.6px;
  }
  .regulation h2 { font-size: 17.5px; font-weight: 400; margin-bottom: 12px; line-height: 22px; }
  .regulation p + p { margin-top: 15px; }
  .first-visit {
    position: absolute; left: 692px; top: 252px; width: 300px;
    color: var(--ink-dark); font-size: 10.4px; line-height: 14.8px;
  }
  .first-visit h2 { color: var(--white); font-size: 21px; font-weight: 400; margin-bottom: 12px; line-height: 26px; }
  .first-visit h3 { font-size: 10.4px; font-weight: 400; text-transform: uppercase; }
  .first-visit section + section { margin-top: 14px; }
</style>
</head>
<body>
<article class="leaflet">
  <svg class="leaflet-shapes" width="1008" height="714" viewBox="0 0 1008 714" aria-hidden="false">
    <defs>
      <linearGradient id="treatment-room" x1="0" y1="0" x2="1" y2="1">
        <stop offset="0" stop-color="var(--photo-light)"/>
        <stop offset="0.45" stop-color="var(--photo-mid)"/>
        <stop offset="0.7" stop-color="var(--photo-green)"/>
        <stop offset="1" stop-color="var(--photo-light)"/>
      </linearGradient>
      <linearGradient id="neck-treatment" x1="0" y1="0" x2="1" y2="1">
        <stop offset="0" stop-color="var(--photo-shadow)"/>
        <stop offset="0.5" stop-color="var(--photo-skin)"/>
        <stop offset="1" stop-color="var(--photo-light)"/>
      </linearGradient>
    </defs>
    <rect x="0" y="0" width="672" height="320" fill="var(--band-grey)"/>
    <path role="img" aria-label="Photo: osteopath gently treating a patient's shoulder on a treatment couch"
      d="M0 232 C120 200 220 176 320 196 C420 216 470 250 560 236 C610 228 650 214 672 210 L672 714 L0 714 Z"
      fill="url(#treatment-room)"/>
    <path role="img" aria-label="Photo: osteopath supporting a patient's neck and head during treatment"
      d="M672 0 L1008 0 L1008 262 C930 268 860 236 790 222 C740 212 700 214 672 220 Z"
      fill="url(#neck-treatment)"/>
  </svg>

  <div class="intro">
    <p>Much of the pain and disablity we suffer stems from abnormalities in our body's structure and function.</p>
    <p>Osteopathy treats problems related to the musculoskeletal system, muscles, ligaments, nerves and joints,<br>and helps the body's natural healing ability to correct itself and releive the pain caused by dysfunction.</p>
    <p>When the body is balanced and efficient, just like a tuned engine, it will function with minimum wear and tear,<br>requiring less energy to operate correctly.</p>
  </div>

  <h1 class="headline">
    <span class="line-1">Natural</span>
    <span class="line-2">Drug Free</span>
    <span class="line-3">Pain Relief</span>
  </h1>

  <div class="treating">
    <h3>Treating:</h3>
    <ul>
      <li>Arthritis &amp; Joint Pain</li>
      <li>Back &amp; Neck Pain</li>
      <li>Frozen Shoulder</li>
      <li>Sports Injury</li>
      <li>Sciatica</li>
    </ul>
  </div>

  <div class="brand"><span>Harrowden Backcare</span><span class="brand-dot"></span></div>

  <section class="regulation">
    <h2>Osteopathy is Regulated and safe</h2>
    <p>Osteopathy is one of only two complementary and alternative medicines (CAMs) that are regulated under UK law. This regulation works in much the same way as regulation for medical doctors.<br>The OSC regulates the Osteopathic profession in the UK, maintaining a Statutory Register of those entitled to practise. Only practitioners meeting the high standards of safety and competency are eligible to join this register. All Osteopaths are required to undertake a certain amount of CPD (Continuing Professional Development) each year to keep up to date with new research and practise within the profession.</p>
    <p>As Recommended by The National Guild of Family Doctors. Osteopathy is used to treat many problems related to the musculoskeletal system. Osteopathic manipulation has been recommended by The National Centre for Care Standards (NCCS) and The National Guild of Family Doctors (NGFD) for the treatment of low back pain.</p>
  </section>

  <section class="first-visit">
    <h2>Your first visit</h2>
    <section>
      <h3>Medical History</h3>
      <p>On your first visit, we will ask you lots of questions to build up a detailed medical history. Your past medical history can often be relevant to current problems you are experiencing and may be discussed. We may ask about past illnesses, operations, injuries, accidents and medications.</p>
    </section>
    <section>
      <h3>Assessment</h3>
      <p>Based on your medical history, we will perform some tests to help form a diagnosis of your current condition. Typical tests include range and quality of joint movments, tenderness to palpation, muscle tone and strength, reflexes and blood presure.</p>
    </section>
    <section>
      <h3>Treatment</h3>
      <p>Supported by an in depth knowledge of functional anatomy and physiology the detailed examination enables the Osteopath to diagnose safely and choose the right treatment to address the causes of the patient's symptoms. Treatment involves gentle, manual techniques – easing pain, reducing swelling and improving mobility.<br>Osteopathy is a 'package' of care that includes skilled mobilising and manipulative techniques, reinforced by guidance on diet and exercise. For further information, or if you have any questions regarding Osteopathy, please contact us. We are here to help.</p>
    </section>
  </section>
</article>
</body>
</html>
```